Business Card Design

Mortgage brokering company, also providing Commercial Finance, Car Finance and Insurance.

Target Market(s)

Home Buyers

Industry/Entity Type

Business

Contact Information for Business Card

All information required on business card is contained in the attachment. Design does not have to follow the style of the attachment.

```html
<!DOCTYPE html>
<html lang="en">
<head>
<meta charset="utf-8">
<title>BRN Mortgage Services – Business Card</title>
<link rel="stylesheet" href="https://fonts.googleapis.com/css2?family=Arimo:wght@400;700&display=swap">
<style>
  :root {
    --backdrop: #cfcfcf;
    --card: #1b1b1b;
    --card-edge: #262626;
    --orange: #f7941d;
    --brand-text: #b5b5b5;
    --white: #f2f2f2;
  }
  * { box-sizing: border-box; margin: 0; padding: 0; }
  html, body { width: 1200px; height: 819px; overflow: hidden; }
  body {
    background: var(--backdrop);
    font-family: "Arimo", Arial, sans-serif;
    position: relative;
  }
  .card {
    position: absolute;
    top: 250px;
    width: 520px;
    height: 318px;
    background: linear-gradient(135deg, var(--card-edge), var(--card) 60%);
    box-shadow: 0 10px 30px rgba(0,0,0,.35);
    color: var(--white);
  }
  .card--front { left: 50px; }
  .card--back { left: 630px; }

  /* front */
  .brand-name {
    position: absolute;
    left: 190px;
    top: 72px;
    color: var(--brand-text);
    font-size: 40px;
    font-weight: 400;
    line-height: 1.05;
  }
  .services-line {
    position: absolute;
    left: 0;
    right: 0;
    top: 220px;
    text-align: center;
    font-size: 15px;
    font-variant: small-caps;
    letter-spacing: 1px;
  }

  /* back */
  .brand-mini {
    position: absolute;
    right: 30px;
    top: 34px;
    text-align: right;
    color: var(--brand-text);
    font-size: 15px;
    font-weight: 400;
    line-height: 1.2;
  }
  .person { position: absolute; right: 30px; top: 110px; text-align: right; }
  .person__name { font-size: 21px; font-weight: 700; font-variant: small-caps; letter-spacing: 1px; }
  .person__role { color: var(--orange); font-size: 13px; margin-top: 2px; }
  .contact {
    position: absolute; right: 30px; top: 180px;
    text-align: right; font-size: 12.5px; line-height: 1.6;
  }
  .contact .label { color: var(--orange); }
  .address {
    position: absolute; right: 30px; top: 245px;
    text-align: right; font-size: 13px; line-height: 1.45;
  }
</style>
</head>
<body>
  <section class="card card--front">
    <div class="brand-name">BRN<br>Mortgage<br>Services</div>
    <p class="services-line">Residential | Asset Finance | Insurance</p>
  </section>

  <section class="card card--back">
    <div class="brand-mini">BRN Mortgage Services</div>
    <div class="person">
      <div class="person__name">Martin Hale</div>
      <div class="person__role">Credit Representative</div>
    </div>
    <div class="contact">
      <div><span class="label">P:</span> 07 5550 1234 | <span class="label">M:</span> 0400 555 012 | <span class="label">F:</span> 07 5550 1235</div>
      <div><span class="label">E:</span> martin.hale@brnmortgage.com.au | <span class="label">W:</span> www.brnmortgage.com.au</div>
    </div>
    <div class="address">14 Harbour View Road,<br>Coral Heights, Qld 4000</div>
  </section>
</body>
</html>
```